Property investment company needs a letterhead design!

We are a new residential and commercial property investment company. Name of the company is Morvesta Group, LLC. We have a new logo and now we need letterhead! We prefer to have a professional and upscale appearance. We don't have any fixed requirements, so be creative! Thank you for considering this project. We are so excited to see what happens!

Target Market(s)

Professional

Industry/Entity Type

Real Estate Development

```html
<!DOCTYPE html>
<html lang="en">
<head>
<meta charset="utf-8">
<title>Morvesta Group, LLC — Letterhead</title>
<link rel="stylesheet" href="https://fonts.googleapis.com/css2?family=Lato:wght@300;400&family=Montserrat:wght@700&family=Roboto+Condensed:wght@300;400&display=swap">
<style>
  :root {
    --backdrop: #d6d6d6;
    --paper: #ffffff;
    --navy: #0f2340;
    --accent: #1ba0e2;
    --text: #555555;
    --heading: #5a5a5a;
  }
  html, body {
    margin: 0;
    width: 1056px;
    height: 1200px;
    overflow: hidden;
    background: var(--backdrop);
  }
  .letterhead {
    position: absolute;
    left: 118px;
    top: 20px;
    width: 820px;
    height: 1160px;
    background: var(--paper);
    overflow: hidden;
    box-shadow: 0 12px 30px rgba(0,0,0,0.18);
  }
  .brand {
    position: absolute;
    left: 77px;
    top: 112px;
    display: flex;
    align-items: center;
    gap: 12px;
  }
  .brand-dot {
    width: 38px;
    height: 38px;
    border-radius: 50%;
    background: var(--navy);
  }
  .brand-name {
    font-family: "Montserrat", sans-serif;
    font-weight: 700;
    font-size: 22px;
    letter-spacing: 0.5px;
    color: var(--navy);
    text-transform: uppercase;
  }
  .contact {
    position: absolute;
    left: 578px;
    top: 76px;
    font-family: "Lato", sans-serif;
    font-style: normal;
    font-weight: 400;
    font-size: 15px;
    color: var(--text);
  }
  .contact .address { margin: 0 0 11px; line-height: 18.5px; }
  .contact ul { list-style: none; margin: 0; padding: 0; }
  .contact li {
    display: flex;
    align-items: center;
    gap: 14px;
    height: 21px;
  }
  .contact svg { width: 15px; height: 15px; flex: none; }
  .recipient {
    position: absolute;
    left: 77px;
    top: 398px;
    color: var(--heading);
  }
  .recipient .date {
    font-family: "Lato", sans-serif;
    font-weight: 300;
    font-size: 18.5px;
    margin: 0;
  }
  .recipient .name {
    font-family: "Montserrat", sans-serif;
    font-weight: 700;
    font-size: 29px;
    margin: 6px 0 0;
    letter-spacing: 0.2px;
  }
  .recipient .role {
    font-family: "Lato", sans-serif;
    font-weight: 300;
    font-size: 18.5px;
    margin: 4px 0 0;
  }
  .body {
    position: absolute;
    left: 77px;
    top: 542px;
    width: 666px;
    font-family: "Roboto Condensed", sans-serif;
    font-weight: 400;
    font-size: 16px;
    line-height: 28.5px;
    color: var(--text);
  }
  .body p { margin: 0 0 28.5px; text-align: justify; }
  .body p:last-child { text-align: left; }
  .closing {
    position: absolute;
    left: 77px;
    top: 855px;
    font-family: "Roboto Condensed", sans-serif;
    font-weight: 400;
    font-size: 17.5px;
    color: var(--text);
    margin: 0;
  }
  .signature {
    position: absolute;
    left: 77px;
    top: 900px;
    width: 86px;
    height: 60px;
    background: linear-gradient(135deg, #f1f3f6, #e3e7ee);
    border-radius: 4px;
  }
</style>
</head>
<body>
  <main class="letterhead">
    <header>
      <div class="brand">
        <span class="brand-dot" aria-hidden="true"></span>
        <span class="brand-name">Morvesta Group, LLC</span>
      </div>

      <address class="contact">
        <p class="address">1234 First Line Address<br>5678 Second Line Address</p>
        <ul>
          <li>
            <svg viewBox="0 0 24 24" aria-hidden="true"><path fill="var(--accent)" d="M6.6 10.8a15.1 15.1 0 0 0 6.6 6.6l2.2-2.2a1 1 0 0 1 1-.25 11.4 11.4 0 0 0 3.6.57 1 1 0 0 1 1 1V20a1 1 0 0 1-1 1A17 17 0 0 1 3 4a1 1 0 0 1 1-1h3.5a1 1 0 0 1 1 1c0 1.25.2 2.45.57 3.57a1 1 0 0 1-.25 1z"/></svg>
            +888 6666 9999
          </li>
          <li>
            <svg viewBox="0 0 24 24" aria-hidden="true"><rect x="2" y="5" width="20" height="14" fill="var(--accent)"/><path d="M2 5l10 8 10-8" fill="none" stroke="#fff" stroke-width="1.6"/></svg>
            info@yourmail.com
          </li>
          <li>
            <svg viewBox="0 0 24 24" aria-hidden="true" fill="none" stroke="var(--accent)" stroke-width="1.6"><circle cx="12" cy="12" r="9.5"/><ellipse cx="12" cy="12" rx="4" ry="9.5"/><path d="M2.5 12h19M4 7h16M4 17h16"/></svg>
            www.yourwebsite.com
          </li>
        </ul>
      </address>
    </header>

    <section class="recipient">
      <p class="date">10 December, 2021</p>
      <h1 class="name">MICHAEL SMITH</h1>
      <p class="role">Cheif Executive Officer</p>
    </section>

    <section class="body">
      <p>Contrary to popular belief, Lorem Ipsum is not simply random text. It has roots in a piece of classical Latin literature from 45 BC, making it over 2000 years old. Daniel Ostrander, a Latin professor at Harwell College in Vermont, looked up one of the more obscure Latin words, consectetur.</p>
      <p>Lorem Ipsum comes from sections 1.10.32 and 1.10.33 of "de Finibus Bonorum et Malorum" (The Extremes of Good and Evil) by Cicero, written in 45 BC. This book is a treatise on the theory of ethics, very popular during the Renaissance. The first line of Lorem Ipsum.</p>
      <p>The standard chunk of Lorem Ipsum used since the 1500s is reproduced below for those interested.</p>
    </section>

    <p class="closing">Best Regards</p>
    <div class="signature" role="img" aria-label="Handwritten signature of Michael Smith"></div>
  </main>
</body>
</html>
```